Land Development Company Website Redesign

We are looking for a fresh design for our website. The content will remain 90% the same.

We really like the layout style of www.quibbenstor.com.

We have attached our current site for content.

Industry/Entity Type

Real Estate Development

Coding

Coded - Design and coding required

Number of Pages Required

5+ page

Font styles to use
Sans Serif

Requirements
Must have
• Consistent feel across all the pages. Visually appealing and simple layout design that can be viewed on a mobile device and browser.

```html
<!DOCTYPE html>
<html lang="en">
<head>
<meta charset="utf-8">
<title>Ashbrook Estates – What's New</title>
<link href="https://fonts.googleapis.com/css2?family=Roboto+Condensed:wght@400;700&family=Arimo:wght@400;700&display=swap" rel="stylesheet">
<style>
  :root {
    --gold: #d4a960;
    --gold-box: #d5ae6b;
    --maroon: #6a0d1f;
    --ink: #1b1b1b;
    --body-ink: #2b2623;
    --sand: #eadbbf;
    --panel: #f6eee0;
    --white: #ffffff;
    --frame: #8b2a2a;
  }
  * { box-sizing: border-box; margin: 0; padding: 0; }
  html, body { width: 1200px; height: 1101px; overflow: hidden; }
  body {
    position: relative;
    background: var(--sand);
    font-family: "Roboto Condensed", "Arial Narrow", sans-serif;
    color: var(--ink);
  }
  .top-rule { position: absolute; top: 0; left: 0; width: 1200px; height: 5px; background: var(--gold); }
  .site-header { position: absolute; top: 5px; left: 0; width: 1200px; height: 82px; background: var(--white); }
  .brand {
    position: absolute; left: 232px; top: 20px;
    display: flex; align-items: center; gap: 8px;
    font-size: 18px; font-weight: 700; color: var(--ink); letter-spacing: 0.5px;
  }
  .brand-mark { width: 14px; height: 14px; background: var(--gold); }
  .main-nav a, .footer-nav a { position: absolute; text-decoration: none; white-space: nowrap; }
  .main-nav a { top: 32px; font-size: 11.5px; color: var(--ink); }
  .main-nav a.is-active { color: #c98a2a; }
  .hero {
    position: absolute; top: 87px; left: 0; width: 1200px; height: 244px;
    background: linear-gradient(180deg, #c9d6e6 0%, #b0542f 35%, #8a3a26 60%, #4f6b2e 85%, #c8c04a 100%);
  }
  .page-backdrop {
    position: absolute; top: 331px; left: 0; width: 1200px; height: 710px;
    background: linear-gradient(180deg, #eadcc0 0%, #e6d5b6 100%);
  }
  .content-panel { position: absolute; top: 331px; left: 225px; width: 750px; height: 710px; background: var(--panel); }
  .news-box { position: absolute; top: 354px; left: 250px; width: 194px; height: 221px; background: var(--gold-box); }
  .news-box h2 {
    font-weight: 400; font-size: 15px; color: var(--ink);
    padding: 14px 0 4px 12px; border-bottom: 1px solid #e7cc9a;
  }
  .news-list { list-style: none; padding: 12px 0 0 13px; }
  .news-item { position: relative; padding-left: 13px; margin-bottom: 12px; font-family: "Arimo", Arial, sans-serif; font-size: 8.5px; line-height: 11px; color: var(--maroon); letter-spacing: 0.4px; }
  .news-item::before, .press-link::before {
    content: ""; position: absolute; left: 0; top: 3px;
    border-left: 7px solid var(--maroon); border-top: 4px solid transparent; border-bottom: 4px solid transparent;
  }
  .news-item strong { display: block; font-size: 9px; }
  .press-link {
    position: absolute; left: 13px; top: 196px; padding-left: 14px;
    font-family: "Arimo", Arial, sans-serif; font-size: 9px; font-weight: 700; letter-spacing: 0.6px;
    color: var(--ink); text-decoration: underline;
  }
  .press-link::before { border-left-color: var(--ink); top: 2px; }
  .intro { position: absolute; top: 348px; left: 484px; width: 466px; font-size: 12px; line-height: 22px; color: var(--body-ink); }
  .intro p + p { margin-top: 22px; }
  .headline {
    position: absolute; top: 518px; left: 484px; width: 470px;
    font-size: 28px; line-height: 27px; font-weight: 700; color: var(--maroon); letter-spacing: 0.3px;
  }
  .photo { position: absolute; border: 1px solid var(--frame); }
  .estates-title { position: absolute; top: 804px; left: 251px; font-size: 15px; font-weight: 400; }
  .estates-copy { position: absolute; top: 831px; left: 250px; width: 450px; font-size: 12px; line-height: 23.3px; color: var(--ink); }
  .site-footer { position: absolute; top: 1041px; left: 0; width: 1200px; height: 60px; background: var(--white); }
  .footer-nav a { top: 20px; font-family: "Arimo", Arial, sans-serif; font-size: 10.5px; color: var(--ink); }
  .copyright { position: absolute; top: 19px; left: 906px; font-family: "Arimo", Arial, sans-serif; font-size: 9px; color: var(--maroon); }
</style>
</head>
<body>
  <div class="top-rule"></div>
  <header class="site-header">
    <div class="brand"><span class="brand-mark"></span>Ashbrook</div>
    <nav class="main-nav">
      <a class="is-active" href="#" style="left:504px">WHAT'S NEW</a>
      <a href="#" style="left:614px">THE ESTATES</a>
      <a href="#" style="left:718px">THE TEAM</a>
      <a href="#" style="left:810px">GALLERY</a>
      <a href="#" style="left:897px">CONTACT</a>
    </nav>
  </header>

  <div class="hero" role="img" aria-label="Street of brick and half-timbered Tudor-style houses with hedges and parked cars"></div>

  <div class="page-backdrop" role="img" aria-label="Faded sepia view of homes and landscaped gardens"></div>
  <main class="content-panel"></main>

  <aside class="news-box">
    <h2>LATEST NEWS</h2>
    <ul class="news-list">
      <li class="news-item"><strong>Nov 23/15</strong>All future Phases will consist of very limited releases.</li>
      <li class="news-item"><strong>Nov 23/15</strong>All future Phases will consist of very limited releases.</li>
      <li class="news-item"><strong>Nov 23/15</strong>All future Phases will consist of very limited releases.</li>
    </ul>
    <a class="press-link" href="#">VIEW ALL PRESS RELEASES</a>
  </aside>

  <section class="intro">
    <p>Ashbrook Estates at Loma Vista is quickly becoming Clovis' finest custom home community. In spring 2009, 9 of 49 custom homesites will be offering to the public. These lots are impressive with over 90 to 100 feet wide and are ranging from one-quarter to over half an acre in size.</p>
    <p>In order to take advantage of the Pre-Development price, call now to place a fully refundable deposit for a reservation of these home sites.</p>
  </section>

  <h1 class="headline">HURRY ONLY THREE CUSTOM LOTS ARE AVAILABLE!</h1>

  <div class="photo" style="top:615px;left:251px;width:216px;height:156px;background:linear-gradient(180deg,#8fa3c4 0%,#b89a5a 45%,#6e5a3a 75%,#3f6a2a 100%)" role="img" aria-label="Ochre stucco cottage behind a bare tree"></div>
  <div class="photo" style="top:615px;left:490px;width:217px;height:156px;background:radial-gradient(circle at 50% 30%,#e3a660 0%,#8a4a20 55%,#3a1a0c 100%)" role="img" aria-label="Warm wood-panelled dining room and kitchen with chandelier"></div>
  <div class="photo" style="top:615px;left:732px;width:216px;height:156px;background:linear-gradient(180deg,#dfe8f2 0%,#b59c82 40%,#9a8670 70%,#4f8a2c 100%)" role="img" aria-label="Two-storey stucco home with tiled roof and green lawn"></div>

  <h2 class="estates-title">THE ESTATES</h2>
  <p class="estates-copy">Looking for the perfect new community in Clovis, California? There's no better location than Ashbrook Estates, an exclusive luxury custom home community nestled in the heart of Loma Vista, A Clovis Community with easy access to the best that Fresno/Clovis region has to offer. Within a few miles of this pristine community are an abundance of amenities including trails, parks, and lakes. The Valley Ridge Innovation Park, a newly expanded Orchard Commons Mall, and Northgate Medical Center are only a few miles away with easy access to Highway 168.</p>

  <div class="photo" style="top:835px;left:732px;width:216px;height:156px;background:linear-gradient(180deg,#cfd9d6 0%,#7d6a58 40%,#c97aa4 65%,#5c9a36 100%)" role="img" aria-label="House with dark roof surrounded by pink flowering shrubs and lawn"></div>

  <footer class="site-footer">
    <nav class="footer-nav">
      <a href="#" style="left:230px">WHAT'S NEW</a>
      <a href="#" style="left:328px">THE ESTATES</a>
      <a href="#" style="left:432px">THE TEAM</a>
      <a href="#" style="left:519px">GALLERY</a>
      <a href="#" style="left:612px">CONTACT</a>
    </nav>
    <p class="copyright">all right reserved</p>
  </footer>
</body>
</html>
```